Quillory Points website re-design and

the institute of massage therapy is ready for a new website. The current website is around 12 years old and it looks old. Luckily the clients is not against changing the colors so the new design does not have to use the current ugly green color scheme. Be creative! Make it pretty, modern and inviting. The current colors look like mold. Nobody likes mold. I have attached the logo asset file as well as a txt document that details the new website design parameters

1 page

```html
<!DOCTYPE html>
<html lang="en">
<head>
<meta charset="utf-8">
<title>Institute of Larkwell Therapy — Continuing Education</title>
<link href="https://fonts.googleapis.com/css2?family=Josefin+Sans:wght@300;400;600;700&display=swap" rel="stylesheet">
<style>
:root{
  --rose:#b98a8d;
  --blush:#d1b4b9;
  --cream:#fcf3f5;
  --backdrop:#f4ebed;
  --ink:#3b3032;
  --muted:#7d7073;
  --line:#ece2e4;
  --white:#ffffff;
}
*{box-sizing:border-box;margin:0;padding:0}
html,body{width:1200px;height:3748px;overflow:hidden}
body{background:var(--backdrop);font-family:'Josefin Sans',sans-serif;color:var(--ink)}
.page{position:absolute;left:137px;top:0;width:925px;height:3748px;background:var(--white);overflow:hidden}
.abs{position:absolute}

/* top bar + nav */
.topbar{left:0;top:0;width:925px;height:65px;background:var(--rose);color:#fff;font-size:8px}
.topbar .note{position:absolute;left:121px;top:11px}
.topbar .tools{position:absolute;left:748px;top:9px;display:flex;gap:22px;align-items:center}
.nav{left:121px;top:33px;width:681px;height:67px;background:#fff;display:flex;align-items:center;justify-content:space-between;padding:0 24px;z-index:3}
.brand{display:flex;align-items:center;gap:8px;color:var(--rose);font-weight:400;line-height:1.05}
.brand-dot{width:16px;height:16px;border-radius:50%;background:var(--rose)}
.brand small{display:block;font-size:7px;letter-spacing:.5px}
.brand span{font-size:12px;letter-spacing:.4px}
.nav ul{list-style:none;display:flex;gap:22px;font-size:9.5px;color:var(--muted)}

/* hero */
.hero{left:0;top:65px;width:925px;height:650px;background:var(--cream);border-bottom-left-radius:55% 130px;overflow:hidden}
.hero-photo{position:absolute;left:0;top:0;width:925px;height:650px;
  background:linear-gradient(100deg,var(--cream) 0%,#f6e4e3 28%,#ecd0c6 48%,#dfb8a6 62%,#efdad0 80%,#f8efe9 100%)}
.hero-kicker{left:118px;top:352px;transform:rotate(-90deg);transform-origin:left top;font-size:7.5px;letter-spacing:2px;color:var(--blush);white-space:nowrap}
.hero h1{left:145px;top:236px;font-weight:400;font-size:31px;line-height:40px;color:var(--ink)}
.hero h1 em{font-style:normal;color:var(--rose)}
.down{left:145px;top:391px;width:40px;height:40px;border-radius:50%;background:var(--blush)}

/* search */
.search{left:121px;top:567px;width:681px;height:125px;background:#fff;border-bottom:1px solid var(--line);display:flex;align-items:center;padding:0 46px;gap:22px;z-index:2}
.search h3{font-weight:400;font-size:12px;line-height:15px;width:120px}
.field{width:135px;height:32px;border-radius:16px;border:1px solid var(--line);background:var(--cream);font-size:7px;color:var(--blush);padding:0 14px;display:flex;align-items:center;justify-content:space-between}
.btn{background:var(--rose);color:#fff;border-radius:16px;font-size:7.5px;letter-spacing:.5px;display:flex;align-items:center;justify-content:center}
.search .btn{width:135px;height:32px}

/* intro */
.label{font-size:7.5px;letter-spacing:2px;color:var(--blush);text-transform:uppercase}
.intro-label{left:121px;top:771px}
.intro h2{left:121px;top:786px;font-weight:300;font-size:31px;line-height:38px}
.intro h2 b{font-weight:600}
.intro-text{left:470px;top:765px;width:333px;font-size:8.5px;line-height:18.5px;color:var(--muted)}
.intro-text p+p{margin-top:22px}
.intro-btn{left:470px;top:1041px;width:79px;height:31px;background:var(--blush);font-size:7px}
.intro-photo{left:121px;top:894px;width:274px;height:322px;background:linear-gradient(160deg,#f1ece8 0%,#e6d6cc 45%,#d9b9a6 75%,#c99e8c 100%);z-index:2}
.intro-photo::after{content:"";position:absolute;inset:10px;border:1px solid rgba(255,255,255,.85)}

/* why band */
.why{left:56px;top:1131px;width:809px;height:339px;background:var(--rose);color:#fff}
.why h2{position:absolute;right:66px;top:70px;font-weight:300;font-size:30px}
.why h2 b{font-weight:600}
.why-item{position:absolute;top:133px;width:150px}
.why-item h4{font-size:9px;font-weight:600;letter-spacing:.3px}
.why-item p{margin-top:12px;font-size:7.5px;line-height:18.5px;opacity:.9}
.why-item i{display:block;margin-top:12px;font-style:normal;font-size:12px}

/* popular courses */
.pop-label{left:121px;top:1594px}
.pop h2{left:121px;top:1611px;font-weight:300;font-size:29px;line-height:33px}
.pop h2 b{font-weight:400}
.circle-btn{top:1704px;width:27px;height:27px;border-radius:50%;background:var(--blush);color:#fff;font-size:12px;display:flex;align-items:center;justify-content:center}
.card{top:1528px;width:214px;height:266px;background:#fff;box-shadow:0 4px 18px rgba(185,138,141,.18);padding:10px}
.card .ph{height:123px}
.card h5{margin-top:18px;font-weight:400;font-size:11px;color:var(--rose)}
.card p{margin-top:10px;font-size:7.5px;line-height:16px;color:var(--muted)}
.card i{display:block;margin-top:10px;font-style:normal;color:var(--blush);font-size:11px}

/* contact banner */
.contact{left:56px;top:1852px;width:809px;height:173px;background:var(--cream)}
.contact p{position:absolute;left:66px;top:58px;width:380px;font-size:13.5px;line-height:23px;color:var(--rose)}
.contact u{text-decoration:underline}
.contact-photo{left:553px;top:1871px;width:372px;height:193px;background:radial-gradient(ellipse at 40% 55%,#ffffff 0%,#f4e3e3 40%,#e7b8bc 65%,rgba(255,255,255,0) 80%)}

/* faq */
.faq-label{left:0;width:925px;top:2098px;text-align:center}
.faq h2{left:0;width:925px;top:2112px;text-align:center;font-weight:300;font-size:31px}
.faq h2 b{font-weight:600}
.faq-col{top:2173px;width:326px}
.faq-item{border-bottom:1px solid var(--line);padding:10px 20px 10px 0;position:relative;font-size:8.5px;line-height:18.5px}
.faq-item::after{content:"+";position:absolute;right:0;top:10px;color:var(--blush);font-size:12px}
.faq-item.open{color:var(--rose)}
.faq-item.open::after{content:"–"}
.faq-item .ans{color:var(--muted);font-size:7.5px;line-height:18px;margin-top:8px}

/* free course */
.free-band{left:56px;top:2526px;width:809px;height:338px;background:var(--cream)}
.free-label{left:121px;top:2586px}
.free-title{left:121px;top:2603px;font-weight:300;font-size:29px}
.free-title b{font-weight:600}
.free-text{left:121px;top:2655px;width:340px;font-size:8.5px;line-height:18.5px;color:var(--muted)}
.free-text p+p{margin-top:8px}
.free-btn{left:121px;top:2775px;width:79px;height:30px;font-size:7px}
.play{left:214px;top:2775px;width:30px;height:30px;border-radius:50%;border:1px solid var(--blush)}
.play svg{position:absolute;left:11px;top:9px}
.free-photo{left:543px;top:2584px;width:270px;height:312px;background:linear-gradient(160deg,#eef0f4 0%,#dfe3ea 40%,#c7cbd6 70%,#b8a6a8 100%)}
.free-photo::after{content:"";position:absolute;inset:10px;border:1px solid rgba(255,255,255,.85)}
.badge{left:476px;top:2835px;width:64px;height:64px;border-radius:50%;border:1px dashed var(--rose)}

/* titles grid */
.titles-label{left:0;width:925px;top:2962px;text-align:center}
.titles h2{left:0;width:925px;top:2977px;text-align:center;font-weight:300;font-size:31px}
.titles h2 b{font-weight:600}
.grid{left:56px;top:3033px;width:809px;display:grid;grid-template-columns:repeat(5,1fr);column-gap:9px;row-gap:9px}
.tile{height:42px;border:1px solid var(--line);padding:6px 26px 0 8px;font-size:7.5px;line-height:12px;color:var(--muted);position:relative}
.tile::after{content:"→";position:absolute;right:8px;top:13px;color:var(--blush);font-size:10px}
.tile.active{background:var(--blush);color:#fff;border-color:var(--blush)}
.tile.active::after{color:#fff}

/* footer */
.footer{left:0;top:3586px;width:925px;height:162px}
.footer svg{position:absolute;left:0;top:0}
.footer .brand{position:absolute;left:104px;top:80px;color:#fff}
.footer .brand-dot{background:#fff}
.footer .links{position:absolute;left:0;width:925px;top:73px;text-align:center;font-size:7.5px;color:#fff;line-height:24px}
.footer .login{position:absolute;left:719px;top:72px;width:79px;height:32px;border-radius:16px;background:#fff;color:var(--rose);font-size:8px;display:flex;align-items:center;justify-content:center}
</style>
</head>
<body>
<main class="page">

  <div class="abs topbar">
    <span class="note">Best online home study continuing education courses available to massage therapists.</span>
    <span class="tools">
      <svg width="11" height="10" viewBox="0 0 11 10" aria-label="Cart"><path d="M0 1h2l1.5 5.5h5.5L10.5 2.5H3" fill="none" stroke="#fff" stroke-width="1.2"/><circle cx="4" cy="8.5" r="1" fill="#fff"/><circle cx="8.5" cy="8.5" r="1" fill="#fff"/></svg>
      <span>Login</span>
    </span>
  </div>

  <section class="abs hero">
    <div class="hero-photo" role="img" aria-label="Photo of a woman relaxing while receiving a shoulder massage"></div>
    <span class="abs hero-kicker">WELCOME TO ILT</span>
    <h1 class="abs">Committed to Excellence<br>in <em>Massage Therapy</em><br>Continuing Education</h1>
    <div class="abs down">
      <svg width="40" height="40" viewBox="0 0 40 40"><path d="M20 13v14M15 22l5 5 5-5" fill="none" stroke="#fff" stroke-width="1.4"/></svg>
    </div>
  </section>

  <nav class="abs nav">
    <div class="brand"><i class="brand-dot"></i><div><small>INSTITUTE OF</small><span>LARKWELL THERAPY</span></div></div>
    <ul><li>Home</li><li>Courses</li><li>Guidelines</li><li>FAQs</li><li>Policies</li><li>Contact</li><li>About</li></ul>
  </nav>

  <form class="abs search">
    <h3>SEARCH NOW FOR ONLINE COURSES</h3>
    <div class="field">Search by Keyword</div>
    <div class="field">Number of CE Hours <span>⌄</span></div>
    <div class="btn">SEARCH NOW</div>
  </form>

  <section class="intro">
    <span class="abs label intro-label">Introduction</span>
    <h2 class="abs">The Institute of<br><b>Larkwell Therapy</b></h2>
    <div class="abs intro-text">
      <p>The Institute of Larkwell Therapy is committed to providing the best online home study continuing education courses available to massage therapists. Institute of Larkwell Therapy is approved by the National Bodywork Credential Council (NBCC) as a continuing education Approved Provider. Provider # 400000-00.</p>
      <p>Our massage CEUs/credits are also valid for AMTC and BMPA. We are approved by the State Board of Bodywork (Provider #MCE000) and CE Tracker (Provider #00-0000). Our massage therapy continuing education courses are valid for most state massage therapy CEU requirements. See our State Guidelines page for specific information about the continuing education laws in your state.</p>
    </div>
    <div class="abs btn intro-btn">ABOUT US</div>
    <div class="abs intro-photo" role="img" aria-label="Photo of hands massaging a client's lower back"></div>
  </section>

  <section class="abs why">
    <h2>Why Choosing <b>ILT?</b></h2>
    <div class="why-item" style="left:65px"><h4>01 - INSTANT ACCESS</h4><p>Simply enroll in any of our online continuing education courses and you will have instant access to your course. As soon as you pass your test, you can print your certificate instantly.</p><i>→</i></div>
    <div class="why-item" style="left:247px"><h4>02 - HASSLE FREE</h4><p>With our online courses, you work at your own pace. Fit your CEUs into your independent lifestyle. You can log in and out as much as you like while taking any course.</p><i>→</i></div>
    <div class="why-item" style="left:424px"><h4>03 - RISK FREE</h4><p>Take a free course to see exactly how our system operates. This gives you the peace of mind of knowing what to expect before you commit to any of our courses.</p><i>→</i></div>
    <div class="why-item" style="left:603px"><h4>04 - 10% TO CHARITY</h4><p>Another reason to take our home study continuing education courses. We donate 10% of profits to charities and organizations. By doing business with us, you help to support value.</p><i>→</i></div>
  </section>

  <section class="pop">
    <span class="abs label pop-label">Our Courses</span>
    <h2 class="abs">Popular<br><b>Courses</b></h2>
    <div class="abs circle-btn" style="left:137px">←</div>
    <div class="abs circle-btn" style="left:175px;background:var(--rose)">→</div>
    <article class="abs card" style="left:355px">
      <div class="ph" role="img" aria-label="Photo of a couple practicing prenatal massage at home" style="background:linear-gradient(135deg,#f4ece6,#e3cfc3 55%,#cdb3a6)"></div>
      <h5>Pregnancy / Doula</h5><p>Courses and packages to become certified in every stage of childbearing, from infertility to infant massage</p><i>→</i>
    </article>
    <article class="abs card" style="left:586px">
      <div class="ph" role="img" aria-label="Photo of a woman receiving a facial massage" style="background:linear-gradient(135deg,#f3e3e4,#e9d3cf 50%,#d6b39f)"></div>
      <h5>Florida Laws &amp; Packages</h5><p>Courses and packages required to obtain, reinstate, or renew your Florida massage therapy license</p><i>→</i>
    </article>
    <article class="abs card" style="left:817px">
      <div class="ph" role="img" aria-label="Photo of a smiling instructor at a desk" style="background:linear-gradient(135deg,#eae6e4,#d8c6bd 55%,#b98a8d)"></div>
      <h5>Research Courses</h5><p>Courses approved by the mandated research hours for renewal</p><i>→</i>
    </article>
  </section>

  <section class="abs contact">
    <p>Please feel free to <u>contact us</u> if you have any questions about how we can help you attain your continuing education goals. Thank you.</p>
  </section>
  <div class="abs contact-photo" role="img" aria-label="Photo of rolled spa towels, rose petals and massage oil"></div>

  <section class="faq">
    <span class="abs label faq-label">FAQ's</span>
    <h2 class="abs">About Our <b>Online Courses</b></h2>
    <div class="abs faq-col" style="left:121px">
      <div class="faq-item">I am currently in massage school. Can I start taking your pregnancy massage course now so when I become licensed I'll be ready to work on pregnant women?</div>
      <div class="faq-item open">Are your online courses straightly downloadable to my personal computer?<div class="ans">No. You must be logged in on our website to view the course materials. We invite you to take our free sample course, Shoulder Dysfunction, to see how our online courses and testing works.</div></div>
      <div class="faq-item">How do I print an additional certificate?</div>
      <div class="faq-item">Does the Institute of Larkwell Therapy automatically report course completions to CE Tracker?</div>
    </div>
    <div class="abs faq-col" style="left:478px">
      <div class="faq-item">Does the Institute of Larkwell Therapy report our course completions to the NBCC, AMTC, BMPA, etc, or any other agencies or state massage therapy boards?</div>
      <div class="faq-item open">Can I log in and out while taking an online course, or do I have to take it all at once?<div class="ans">You are able to log in and out as much as you need while taking a course. Once you start the test, however, you do need to finish it, or you will have to restart the next time you log in.</div></div>
      <div class="faq-item">Will your online courses work on phone, tablet, or other device?</div>
      <div class="faq-item">Do I have to be a licensed massage therapist or something to take your courses?</div>
    </div>
  </section>

  <section class="free">
    <div class="abs free-band"></div>
    <span class="abs label free-label">Take advantage of opportunity</span>
    <h2 class="abs free-title">Take now <b>a Free Course</b></h2>
    <div class="abs free-text">
      <p>Lorem ipsum dolor sit amet, consectetur adipiscing elit, sed do eiusmod tempor incididunt ut labore et dolore magna aliqua. Quis ipsum suspendisse ultrices gravida. Risus commodo viverra maecenas accumsan lacus vel facilisis.</p>
      <p>Quis ipsum suspendisse ultrices gravida. Risus commodo viverra maecenas accumsan lacus vel facilisis.</p>
    </div>
    <div class="abs btn free-btn">GET STARTED</div>
    <div class="abs play"><svg width="9" height="11" viewBox="0 0 9 11"><path d="M0 0l9 5.5L0 11z" fill="#d1b4b9"/></svg></div>
    <div class="abs badge"></div>
    <div class="abs free-photo" role="img" aria-label="Photo of a smiling therapist in scrubs writing at a desk"></div>
  </section>

  <section class="titles">
    <span class="abs label titles-label">Our Certifications</span>
    <h2 class="abs">Available <b>Titles</b></h2>
    <div class="abs grid">
      <div class="tile">Certified Fertility Massage Therapist</div>
      <div class="tile">Certified Infant Massage Therapist/Instructor</div>
      <div class="tile">Certified Massage Doula</div>
      <div class="tile">Certified Prenatal Massage Therapist</div>
      <div class="tile">Customize Your Own Package</div>

      <div class="tile">100 CE Package</div>
      <div class="tile active">Positional Release Fascial Lines</div>
      <div class="tile">Aromatherapy for Massage</div>
      <div class="tile">Board Certified Renewal, Package 1</div>
      <div class="tile">Board Certified Renewal, Package 2</div>

      <div class="tile">Board Certified Renewal, Package 3</div>
      <div class="tile">Communicable Diseases &amp; HIV</div>
      <div class="tile">Deep Tissue Therapy</div>
      <div class="tile">Diversity and Cultural Awareness</div>
      <div class="tile">Draping Your Client (Ethics Standard V)</div>

      <div class="tile">Ethics - Boundary Setting (Standard V)</div>
      <div class="tile">Ethics - Communication</div>
      <div class="tile">Ethics - Confidentiality</div>
      <div class="tile">Ethics - Listening</div>
      <div class="tile">Ethics - Professionalism</div>

      <div class="tile">Facilitated PNF Stretching</div>
      <div class="tile">Fibromyalgia (Stop the Suffering)</div>
      <div class="tile">Florida Laws &amp; Rules - 10 hours #00-000000</div>
      <div class="tile">Florida Laws &amp; Rules - 2 hours #00-00000</div>
      <div class="tile">Florida Renewal &amp; CE - Laws, PME, Ethics</div>

      <div class="tile">Hot Stone Massage</div>
      <div class="tile">Human Trafficking Awareness and Prevention 1 CE</div>
      <div class="tile">Human Trafficking Awareness and Prevention 2 CEs</div>
      <div class="tile">Maryland Package</div>
      <div class="tile">New York Package</div>

      <div class="tile">Orthopedic Massage for the Extremities</div>
      <div class="tile">Orthopedic Massage for the Spine</div>
      <div class="tile">Pathology - Deep Vein Thrombosis</div>
      <div class="tile">Pathology - Edema</div>
      <div class="tile">Pathology - Morton Foot Structure</div>

      <div class="tile">Pathology - Plantar Fasciitis</div>
      <div class="tile">Pathology - Sciatic Pain</div>
      <div class="tile">Pathology - Shoulder Dysfunction</div>
      <div class="tile">Pathology - Varicose Veins</div>
      <div class="tile">Prenatal Massage Fundamentals (Step One)</div>

      <div class="tile">Prenatal Massage Techniques (Step Two)</div>
      <div class="tile">Prevention of Medical Errors for Massage</div>
      <div class="tile">Reflexology for Feet and Hands</div>
      <div class="tile">Research - Infant Massage</div>
      <div class="tile">Research - Pregnancy and Labor Massage</div>

      <div class="tile">Research - Reflexology</div>
      <div class="tile">Seven Mistakes Massage Therapists Make</div>
      <div class="tile">Spa Therapy Techniques</div>
      <div class="tile">Sports &amp; Exercise Massage</div>
      <div class="tile">Stretching Anatomy</div>
    </div>
  </section>

  <footer class="abs footer">
    <svg width="925" height="162" viewBox="0 0 925 162" aria-hidden="true"><path d="M0 60 Q462 -40 925 60 L925 162 L0 162 Z" fill="#b98a8d"/></svg>
    <div class="brand"><i class="brand-dot"></i><div><small>INSTITUTE OF</small><span>LARKWELL THERAPY</span></div></div>
    <div class="links">Sitemap | Privacy Policy | Terms of Use<br>© Copyright 2020 Institute of Larkwell Therapy. All rights reserved.</div>
    <div class="login">Login</div>
  </footer>

</main>
</body>
</html>
```